TovaLamarpe - Israeli Mental Health Website

We are developing an Israeli website for mental health. The website will be both in English and in Hebrew. We have a logo and would like a website design based on the logo and the logos colors (attached).

Attached is a doc that contains the website requirements.

We would like to have an icon for each of the sidebar categories, an image for each of the pages (including each of the sidebar category pages).

Target Market(s)

Adults 18-80

Industry/Entity Type

Mental Health

Number of Pages Required

5+ page

Font styles to use
Sans Serif

Colors

Designer to choose colors to be used in the design.

```html
<!DOCTYPE html>
<html lang="en">
<head>
<meta charset="utf-8">
<title>TovaLamarpe – Mental Health</title>
<link href="https://fonts.googleapis.com/css2?family=Poppins:wght@300;400;500;600;700&display=swap" rel="stylesheet">
<style>
  :root{
    --blue:#1f6fc4;
    --blue-dark:#1b4f9a;
    --green:#5db548;
    --navy:#0e1a36;
    --ink:#2b2f38;
    --muted:#6c7280;
    --band:#f1f3f7;
    --white:#ffffff;
  }
  *{box-sizing:border-box;margin:0;padding:0}
  html,body{width:771px;height:1200px;overflow:hidden}
  body{position:relative;background:var(--white);font-family:"Poppins",Arial,sans-serif;color:var(--ink)}

  /* sidebar */
  .sidebar{position:absolute;left:0;top:0;width:134px;height:424px;background:var(--white);z-index:3;box-shadow:2px 0 8px rgba(0,0,0,.08);padding:14px 10px}
  .brand{display:flex;align-items:center;gap:6px;margin-bottom:16px;white-space:nowrap}
  .brand-dot{width:16px;height:16px;border-radius:50%;background:var(--green);flex:none}
  .brand-name{font-size:13px;font-weight:600;color:var(--blue)}
  .cat-list{list-style:none}
  .cat-list li{display:flex;align-items:center;gap:7px;font-size:8px;font-weight:600;color:var(--ink);line-height:1.15;min-height:24px}
  .cat-list svg{flex:none;width:13px;height:13px}

  /* hero */
  .hero{position:absolute;left:134px;top:0;width:637px;height:411px;background:linear-gradient(120deg,#2a7cc8 0%,#3a9fb4 45%,#6cc27a 100%)}
  .hero-photo{position:absolute;inset:0;background:radial-gradient(ellipse at 55% 35%,rgba(255,255,255,.28),rgba(255,255,255,0) 60%)}
  .nav{position:absolute;top:18px;left:48px;right:18px;display:flex;align-items:center;gap:14px;font-size:9.5px;font-weight:500;color:var(--white);white-space:nowrap}
  .donate{background:var(--blue-dark);padding:7px 16px;border-radius:3px;font-weight:600;margin-left:8px}
  .lang{display:flex;align-items:center;gap:4px;margin-left:4px}
  .hero-title{position:absolute;top:165px;left:0;right:0;text-align:center;color:var(--white);font-size:42px;font-weight:700}
  .hero-sub{position:absolute;top:226px;left:130px;right:130px;text-align:center;color:var(--white);font-size:9.5px;line-height:1.5}
  .scroll-cue{position:absolute;left:50%;top:366px;margin-left:-7px;width:14px;height:22px;border:1.5px solid var(--white);border-radius:8px}
  .scroll-cue::after{content:"";position:absolute;left:5px;top:5px;width:2px;height:5px;background:var(--white);border-radius:1px}

  /* welcome */
  .welcome{position:absolute;left:134px;top:470px;width:637px;text-align:center}
  .welcome h1{font-size:32px;font-weight:400;color:var(--ink)}
  .welcome h1 span{color:var(--blue);font-weight:600}
  .welcome .mark{display:block;width:16px;height:16px;margin:6px auto 8px;border-radius:50%;background:var(--green)}
  .welcome p{font-size:10.5px;line-height:1.55;color:var(--muted);width:470px;margin:0 auto}

  /* emergency */
  .emergency{position:absolute;left:146px;top:660px;width:561px;height:214px;background:var(--white);box-shadow:0 4px 18px rgba(0,0,0,.1);border-radius:4px;display:flex;z-index:2}
  .emergency-photo{flex:none;width:216px;height:214px;border-radius:4px 0 0 4px;background:linear-gradient(135deg,#b9c7d4,#8fa5a8)}
  .emergency-body{padding:32px 22px 0}
  .emergency-body h2{font-size:14px;font-weight:600;margin-bottom:10px}
  .emergency-body p{font-size:10px;line-height:1.55;color:var(--muted);margin-bottom:14px}
  .btn{display:inline-block;color:var(--white);font-size:9.5px;font-weight:600;padding:7px 14px;border-radius:3px;white-space:nowrap}
  .btn-green{background:var(--green)}
  .btn-blue{background:var(--blue)}

  /* services */
  .band{position:absolute;left:0;top:885px;width:771px;height:272px;background:var(--band)}
  .services{position:absolute;left:146px;top:908px;width:561px;display:flex;justify-content:space-between}
  .service{width:126px;text-align:center}
  .service-photo{height:86px;border-radius:3px}
  .service h3{font-size:12.5px;font-weight:600;margin:6px 0 2px}
  .service p{font-size:8.5px;line-height:1.4;color:var(--muted);margin-bottom:7px}
  .service .btn{padding:6px 12px;font-size:9px;display:inline-flex;align-items:center;gap:5px}

  /* footer */
  .footer{position:absolute;left:0;top:1157px;width:771px;height:43px;background:var(--navy);display:flex;align-items:center;padding:0 22px;font-size:8.5px;color:#c5cbd8}
  .footer .name{color:var(--green);font-weight:600;margin-right:4px}
  .footer-links{margin-left:90px;display:flex;gap:26px}
</style>
</head>
<body>

<aside class="sidebar">
  <div class="brand"><span class="brand-dot"></span><span class="brand-name">TovaLamarpe</span></div>
  <ul class="cat-list">
    <li><svg viewBox="0 0 14 14"><circle cx="7" cy="7" r="5.5" fill="none" stroke="#1f6fc4" stroke-width="1.4"/><path d="M7 4v3.5M7 9.5v.5" stroke="#1f6fc4" stroke-width="1.4"/></svg>Emergency Mental Help</li>
    <li><svg viewBox="0 0 14 14"><circle cx="7" cy="7" r="5.5" fill="none" stroke="#1f6fc4" stroke-width="1.4"/></svg>Suicide</li>
    <li><svg viewBox="0 0 14 14"><rect x="2" y="2" width="10" height="10" rx="2" fill="none" stroke="#1f6fc4" stroke-width="1.4"/></svg>Sexual Assault/<br>Violence Victims</li>
    <li><svg viewBox="0 0 14 14"><rect x="2" y="2" width="10" height="10" rx="2" fill="none" stroke="#1f6fc4" stroke-width="1.4"/></svg>Sexual Assault/<br>Violence Assaulters</li>
    <li><svg viewBox="0 0 14 14"><path d="M2 10l3-4 3 3 4-6" fill="none" stroke="#1f6fc4" stroke-width="1.4"/></svg>Post Trauma</li>
    <li><svg viewBox="0 0 14 14"><circle cx="7" cy="7" r="5.5" fill="none" stroke="#1f6fc4" stroke-width="1.4"/><path d="M4.5 9.5q2.5-2 5 0" fill="none" stroke="#1f6fc4" stroke-width="1.2"/></svg>Depression</li>
    <li><svg viewBox="0 0 14 14"><path d="M1 7h2l2-4 3 8 2-4h3" fill="none" stroke="#1f6fc4" stroke-width="1.4"/></svg>Anxiety</li>
    <li><svg viewBox="0 0 14 14"><rect x="4" y="2" width="6" height="10" rx="2" fill="none" stroke="#1f6fc4" stroke-width="1.4"/></svg>Addictions</li>
    <li><svg viewBox="0 0 14 14"><path d="M10 2a5 5 0 1 0 2 8 4 4 0 0 1-2-8z" fill="none" stroke="#1f6fc4" stroke-width="1.4"/></svg>Sleep Disorders</li>
    <li><svg viewBox="0 0 14 14"><path d="M4 2v10M10 2v10M4 5h2" fill="none" stroke="#1f6fc4" stroke-width="1.4"/></svg>Eating Disorders</li>
    <li><svg viewBox="0 0 14 14"><circle cx="7" cy="7" r="5.5" fill="none" stroke="#1f6fc4" stroke-width="1.4"/><path d="M7 3.5v7" stroke="#1f6fc4" stroke-width="1.2"/></svg>Financial Problems</li>
    <li><svg viewBox="0 0 14 14"><circle cx="5" cy="5" r="2" fill="none" stroke="#1f6fc4" stroke-width="1.3"/><circle cx="10" cy="7" r="1.5" fill="none" stroke="#1f6fc4" stroke-width="1.3"/><path d="M1.5 12q3.5-5 7 0" fill="none" stroke="#1f6fc4" stroke-width="1.3"/></svg>Parenthood</li>
    <li><svg viewBox="0 0 14 14"><path d="M7 12L2 7a3 3 0 0 1 5-4 3 3 0 0 1 5 4z" fill="none" stroke="#1f6fc4" stroke-width="1.4"/></svg>Relationship</li>
  </ul>
</aside>

<header class="hero">
  <div class="hero-photo" role="img" aria-label="Soft photo of a supportive conversation, tinted blue to green"></div>
  <nav class="nav">
    <span>Smart Chatline</span><span>Therapists</span><span>Organizations</span><span>Videos</span><span>Contact</span><span>About</span>
    <span class="donate">Donate</span>
    <span class="lang"><svg width="13" height="9" viewBox="0 0 13 9"><rect width="13" height="9" fill="#fff"/><rect width="13" height="1.5" y="1.5" fill="#c33"/><rect width="13" height="1.5" y="4.5" fill="#c33"/><rect width="6" height="4.5" fill="#2a4a9a"/></svg>English ⌄</span>
  </nav>
  <div class="hero-title">TovaLamarpe</div>
  <p class="hero-sub">eiusmod tempor incididunt ut labore et dolore magna aliqua. Ut enim ad minim veniam, quis nostrud exercitation ullamco laboris nisi ut al.</p>
  <div class="scroll-cue"></div>
</header>

<section class="welcome">
  <h1>Welcome to <span>TovaLamarpe</span></h1>
  <span class="mark"></span>
  <p>Lorem ipsum dolor sit amet, consectetur adipiscing elit, sed do eiusmod tempor incididunt ut labore et dolore magna aliqua. Ut enim ad minim veniam, quis nostrud exercitation ullamco laboris nisi ut aliquip ex ea commodo consequat.</p>
</section>

<section class="emergency">
  <div class="emergency-photo" role="img" aria-label="Photo of two women in a calm counselling conversation"></div>
  <div class="emergency-body">
    <h2>Emergency Mental Help</h2>
    <p>Lorem ipsum dolor sit amet, consectetur adipiscing elit, sed do eiusmod tempor incididunt ut labore et dolore magna aliqua. Ut enim ad minim veniam, quis nostrud exercitation ullamco laboris nisi ut aliquip ex ea commodo consequat.</p>
    <span class="btn btn-green">More options for Emergency Mental Help</span>
  </div>
</section>

<div class="band"></div>
<section class="services">
  <article class="service">
    <div class="service-photo" role="img" aria-label="Photo of a hand holding a phone with a chat open" style="background:linear-gradient(135deg,#7fb7a6,#3f7f8a)"></div>
    <h3>Smart Chatline</h3>
    <p>Lorem ipsum dolor sit amet, consectetur adipiscing elit.</p>
    <span class="btn btn-blue"><svg width="9" height="9" viewBox="0 0 10 10"><path d="M2 1l2 0 1 2.5-1.2 1a5 5 0 0 0 2.7 2.7l1-1.2L10 7v2a1 1 0 0 1-1 1A9 9 0 0 1 0 2a1 1 0 0 1 1-1z" fill="#fff"/></svg>050-555-0147</span>
  </article>
  <article class="service">
    <div class="service-photo" role="img" aria-label="Photo of a therapist meeting with a client" style="background:linear-gradient(135deg,#d8b893,#9a7a62)"></div>
    <h3>Therapists</h3>
    <p>Lorem ipsum dolor sit amet, consectetur adipiscing elit.</p>
    <span class="btn btn-blue">Find Therapists</span>
  </article>
  <article class="service">
    <div class="service-photo" role="img" aria-label="Photo of a support group sitting together" style="background:linear-gradient(135deg,#c9b7a0,#7c8c7a)"></div>
    <h3>Organizations</h3>
    <p>Lorem ipsum dolor sit amet, consectetur adipiscing elit.</p>
    <span class="btn btn-blue">Find Organizations</span>
  </article>
  <article class="service">
    <div class="service-photo" role="img" aria-label="Photo of a video being watched on a screen" style="background:linear-gradient(135deg,#c7d3e6,#8aa0c4)"></div>
    <h3>Videos</h3>
    <p>Lorem ipsum dolor sit amet, consectetur adipiscing elit.</p>
    <span class="btn btn-blue">Video Library</span>
  </article>
</section>

<footer class="footer">
  <span class="name">TovaLamarpe</span><span>- Organization for Mental Health ©2022</span>
  <div class="footer-links"><span>Privacy Policy</span><span>Terms</span></div>
</footer>

</body>
</html>
```